Business Cards for IT Consulting Company (Managed Service Provider)

I am looking to have some business cards printed and would like some designs. We are an IT Consulting company based in Vancouver BC. I would like a nice clean and modern look to the cards. I have uploaded all the versions of my logo so parts can be used as needed. Here is a snippit from our website homepage:

Kelbrin Systems Ltd. is an IT Solutions Partner located in Vancouver BC, Canada. We offer IT solutions and support to customers in the greater Vancouver Area. With expertise in Quillara platforms, as well as Tovex and Bryn ZPL and over 12 years experience in the IT industry, Kelbrin Systems is dedicated to offering our clients top quality service and products. We take pride in the solutions we offer our customers. The greatest compliment a client can give us is to recommend our services.

Kelbrin Systems Ltd. offers a wide range of IT services from onsite service to remote support and managed service solutions. This allows clients to choose the support path that best suits their company’s needs. Supporting many different sized companies from small to enterprise level over the past 12 years Kelbrin Systems has the experience and expertise needed to ensure things run smoothly. Allowing our clients to focus on doing business.

Revolutionizing the way IT services are delivered.

Kelbrin Systems is dedicated to providing our clients with IT solutions that work and grow with them for years to come. This philosophy helps save money in the long run instead of replacing equipment constantly. Far too often IT solutions are not well thought out and while possibly solving the problem at hand, require replacement due to growth or quality within a very short time frame. Kelbrin Systems takes pride in providing solutions that will last and be able to accommodate growth without the need for replacement.

Industry/Entity Type

Information Technology

Contact Information for Business Card

Kelbrin Systems Ltd.
(Employee Name)
Eml: (Employees Email Address)
Web: kelbrinsys.me
Ph: 604-555-0142

Font styles to use
Serif
Sans Serif

Requirements
Must have
• The Company logo and company colors.
Nice to have
• - Our tag line: "Building IT That Lasts" or "Revolutionizing the way IT services are delivered."
• - Also I really like the idea of nature and technology together blending which is sort of where my logo came from so integrating that somehow onto the business cards would be great.

```html
<!DOCTYPE html>
<html lang="en">
<head>
<meta charset="utf-8">
<title>Kelbrin Systems Ltd. — Business Cards</title>
<link rel="stylesheet" href="https://fonts.googleapis.com/css2?family=Lato:wght@400;700&display=swap">
<style>
  :root {
    --backdrop: #2b2b2d;
    --card-white: #f7f7f7;
    --brand-blue: #29a3dc;
    --brand-blue-deep: #1d86c4;
    --brand-blue-light: #3fb6ea;
    --ink-grey: #5c5c5c;
    --white: #ffffff;
  }
  * { margin: 0; padding: 0; box-sizing: border-box; }
  html, body {
    width: 1200px; height: 997px; overflow: hidden;
    background: var(--backdrop);
    font-family: "Lato", Arial, sans-serif;
  }
  .canvas { position: relative; width: 1200px; height: 997px; }

  .card {
    position: absolute;
    width: 560px; height: 320px;
    box-shadow: 0 18px 40px rgba(0,0,0,0.45);
  }

  /* Contact side */
  .card-front {
    left: 90px; top: 110px;
    background: var(--card-white);
    color: var(--ink-grey);
  }
  .front-brand {
    position: absolute; left: 40px; top: 46px;
    display: flex; align-items: center; gap: 12px;
  }
  .brand-mark {
    flex: none;
    width: 22px; height: 22px;
    border: 2px solid var(--brand-blue);
  }
  .brand-name {
    font-weight: 700; font-size: 28px; line-height: 1;
    color: var(--brand-blue); white-space: nowrap;
  }
  .front-web {
    position: absolute; right: 36px; top: 54px;
    display: flex; align-items: center; gap: 8px;
    font-size: 13px; color: var(--ink-grey);
  }
  .web-dot {
    width: 10px; height: 10px; border-radius: 50%;
    border: 1.5px solid var(--brand-blue);
  }
  .person { position: absolute; left: 40px; top: 150px; }
  .person-name { font-size: 22px; font-weight: 700; color: var(--brand-blue); }
  .person-role { font-size: 13px; color: var(--ink-grey); margin-top: 2px; }
  .contact-list {
    position: absolute; left: 40px; top: 232px;
    list-style: none; font-size: 15px; color: var(--ink-grey);
  }
  .contact-list li { display: flex; align-items: center; gap: 12px; margin-bottom: 10px; }
  .contact-icon { width: 14px; height: 14px; flex: none; }

  /* Brand side */
  .card-back {
    left: 550px; top: 520px;
    overflow: hidden;
  }
  .facet-field {
    position: absolute; inset: 0;
    background: linear-gradient(135deg, var(--brand-blue-light) 0%, var(--brand-blue) 50%, var(--brand-blue-deep) 100%);
  }
  .back-brand {
    position: absolute; left: 0; right: 0; top: 116px;
    display: flex; flex-direction: column; align-items: center;
    color: var(--white);
  }
  .back-brand-row { display: flex; align-items: center; gap: 14px; }
  .back-brand .brand-mark { width: 28px; height: 28px; border-color: var(--white); }
  .back-brand .brand-name { color: var(--white); font-size: 36px; }
  .tagline {
    margin-top: 16px; font-size: 15px; font-weight: 700;
    letter-spacing: 3px; color: var(--white);
  }
</style>
</head>
<body>
<main class="canvas">

  <section class="card card-front" aria-label="Business card, contact side">
    <div class="front-brand">
      <span class="brand-mark"></span>
      <span class="brand-name">Kelbrin Systems Ltd.</span>
    </div>
    <div class="front-web">
      <span>www.kelbrinsys.me</span>
      <span class="web-dot"></span>
    </div>
    <div class="person">
      <p class="person-name">Marla Ostrow</p>
      <p class="person-role">Network Engineer</p>
    </div>
    <ul class="contact-list">
      <li>
        <svg class="contact-icon" viewBox="0 0 14 14" aria-hidden="true">
          <rect x="3" y="1" width="8" height="12" rx="1.5" fill="none" stroke="#29a3dc" stroke-width="1.4"/>
        </svg>
        604-555-0142
      </li>
      <li>
        <svg class="contact-icon" viewBox="0 0 14 14" aria-hidden="true">
          <rect x="1" y="3" width="12" height="8" fill="none" stroke="#29a3dc" stroke-width="1.4"/>
          <polyline points="1,3 7,8 13,3" fill="none" stroke="#29a3dc" stroke-width="1.4"/>
        </svg>
        mostrow@kelbrinsys.me
      </li>
    </ul>
  </section>

  <section class="card card-back" aria-label="Business card, brand side">
    <div class="facet-field" role="img" aria-label="Blue low-poly faceted background pattern"></div>
    <div class="back-brand">
      <div class="back-brand-row">
        <span class="brand-mark"></span>
        <span class="brand-name">Kelbrin Systems Ltd.</span>
      </div>
      <p class="tagline">Building IT That Lasts</p>
    </div>
  </section>

</main>
</body>
</html>
```